KiteDay Fundraiser

I am looking for a fresh design for the 10th annual KiteDay fundraiser. Green and blue colors need to be incorporated . I attached the current flyer. I would like this flyer for September 20, 2020. This is a fundraiser to help find a cure for NF, nuerofibromatosis.

We are looking for a fresh look for the 10th annual event

Target Market(s)

Families and individuals of surrounding areas

Colors
0255a3
add136

Requirements
Must have
• Blue and green colors. It is the 10th annual. The logos of QT CENTER and children’s hospital logo that are shown on the previous flyer I attached
Nice to have
• Eye catching

```html
<!DOCTYPE html>
<html lang="en">
<head>
<meta charset="utf-8">
<title>10th Annual KiteDay</title>
<link rel="stylesheet" href="https://fonts.googleapis.com/css2?family=Anton&family=Roboto+Condensed:wght@400;700&family=Gochi+Hand&display=swap">
<style>
  :root {
    --blue: #0255a3;
    --title-blue: #2a5aa0;
    --green: #7dc14b;
    --green-dark: #5faa35;
    --ink: #3d3d3d;
    --gray: #4d4d4d;
    --orange: #f6a93b;
    --pink: #ec5fa4;
    --sky: #1fa3dd;
    --purple: #8a7dc4;
    --paper: #ffffff;
  }
  * { box-sizing: border-box; margin: 0; padding: 0; }
  html, body { width: 873px; height: 1200px; overflow: hidden; background: #fff; }
  .flyer {
    position: relative; width: 873px; height: 1200px; overflow: hidden;
    font-family: "Roboto Condensed", Arial, sans-serif; color: var(--ink);
  }
  .rainbow-backdrop {
    position: absolute; inset: 0;
    background:
      linear-gradient(160deg, rgba(255,255,255,0) 40%, rgba(255,255,255,.15) 60%, rgba(255,255,255,0) 75%),
      linear-gradient(0deg, #f03f7c 0%, #f5853b 22%, #f9d64f 40%, #cde05a 50%, #22b8c4 66%, #3a8fd6 82%, #4a5ec0 100%);
  }
  .dot-frame {
    position: absolute; left: 30px; top: 30px; width: 813px; height: 1140px;
    border: 7px dotted rgba(255,255,255,.95); border-radius: 36px;
  }
  .panel {
    position: absolute; left: 46px; top: 46px; width: 781px; height: 1108px;
    background: var(--paper); border-radius: 28px;
  }
  .abs { position: absolute; }
  .annual {
    left: 143px; top: 238px; transform-origin: left top; transform: rotate(-90deg);
    font-family: Anton, Impact, sans-serif; font-size: 34px; color: var(--gray);
    letter-spacing: 1px; white-space: nowrap; line-height: 1;
  }
  .event-title {
    left: 195px; top: 58px; width: 560px; text-align: center;
    font-family: Anton, Impact, sans-serif; font-size: 170px; line-height: 1;
    letter-spacing: 1px; font-weight: 400;
    color: var(--title-blue); white-space: nowrap;
  }
  .event-title .accent { color: var(--green); }
  .acronym {
    left: 0; width: 873px; top: 268px; text-align: center;
    font-weight: 700; font-size: 24px; color: var(--gray); letter-spacing: .3px;
  }
  .acronym b { color: var(--green-dark); }
  .info { left: 0; width: 873px; text-align: center; font-weight: 700; font-size: 29px; color: #333; }
  .info-line { display: flex; align-items: center; justify-content: center; gap: 10px; height: 38px; }
  .dot-icon { width: 34px; height: 34px; border-radius: 50%; display: inline-flex; align-items: center; justify-content: center; }
  .features { left: 0; top: 500px; width: 873px; height: 160px; }
  .feature { position: absolute; top: 0; width: 160px; margin-left: -80px; text-align: center; }
  .feature-badge { width: 116px; height: 116px; margin: 0 auto; display: block; }
  .feature-label { font-weight: 700; font-size: 37px; color: var(--gray); margin-top: 6px; letter-spacing: .5px; }
  .activities {
    left: 0; width: 873px; top: 690px; text-align: center;
    font-family: "Gochi Hand", cursive; font-size: 28px; line-height: 38px; color: #222;
  }
  .studio { font-family: Georgia, serif; font-size: 24px; letter-spacing: .5px; }
  .web { left: 160px; top: 858px; display: flex; align-items: center; gap: 12px; font-weight: 700; font-size: 22px; color: #333; }
  .donate-note { left: 0; width: 873px; top: 896px; text-align: center; font-size: 17px; line-height: 26px; color: #333; }
  .contacts { left: 306px; top: 962px; font-weight: 700; font-size: 18px; line-height: 23px; color: #222; border-collapse: collapse; }
  .contacts td { padding: 0; }
  .contacts .sep { padding: 0 8px 0 4px; }
  .phone-icon { left: 249px; top: 987px; }
  .center-mark {
    left: 80px; top: 1080px; display: flex; align-items: center; gap: 8px;
    color: var(--blue); font-weight: 700; font-size: 19px; line-height: 1.05;
  }
  .footnote { left: 210px; top: 1090px; width: 430px; font-size: 12.5px; line-height: 18px; color: #444; }
  .hospital-mark { left: 650px; top: 1080px; display: flex; align-items: center; gap: 8px; color: var(--blue); font-weight: 700; font-size: 19px; line-height: 1.05; }
  .mark-square { width: 16px; height: 16px; background: var(--blue); flex: none; }
</style>
</head>
<body>
<main class="flyer">
  <div class="rainbow-backdrop" role="img" aria-label="Soft rainbow gradient backdrop in pink, orange, yellow, teal and blue"></div>
  <div class="dot-frame"></div>
  <div class="panel"></div>

  <div class="abs annual">10TH ANNUAL</div>
  <h1 class="abs event-title">KITE<span class="accent">DAY</span></h1>

  <p class="abs acronym"><b>M</b>AKE <b>A</b> <b>S</b>TAND <b>O</b>PPOSING <b>N</b>EUROFIBROMATOSIS</p>

  <div class="abs info" style="top:348px">
    <div class="info-line">
      <span class="dot-icon" style="background:var(--orange)">
        <svg width="20" height="20" viewBox="0 0 20 20" fill="none" stroke="#fff" stroke-width="1.6"><rect x="2" y="4" width="16" height="14" rx="1"/><line x1="2" y1="8" x2="18" y2="8"/><line x1="6" y1="2" x2="6" y2="6"/><line x1="14" y1="2" x2="14" y2="6"/></svg>
      </span>
      <span>Sunday, September 20, 2020</span>
      <span class="dot-icon" style="background:var(--pink)">
        <svg width="22" height="22" viewBox="0 0 22 22" fill="none" stroke="#fff" stroke-width="1.8"><circle cx="11" cy="11" r="7.5"/><path d="M11 7v4l3 2"/></svg>
      </span>
      <span>12pm - 6pm</span>
    </div>
    <div class="info-line">Marlow County Fair Grounds</div>
    <div class="info-line">
      <span class="dot-icon" style="background:var(--sky)">
        <svg width="18" height="22" viewBox="0 0 18 22" fill="none" stroke="#fff" stroke-width="1.8"><path d="M9 20s-6-6.5-6-11a6 6 0 0 1 12 0c0 4.5-6 11-6 11z"/><circle cx="9" cy="9" r="2"/></svg>
      </span>
      <span>512 E. Orchard Rd, Glenfield, IL 62000</span>
    </div>
  </div>

  <section class="abs features">
    <div class="feature" style="left:197px">
      <svg class="feature-badge" viewBox="0 0 116 116"><circle cx="58" cy="58" r="54" fill="none" stroke="var(--blue)" stroke-width="3"/><circle cx="58" cy="58" r="47" fill="var(--blue)"/><g stroke="#fff" stroke-width="3" fill="none" stroke-linecap="round"><path d="M38 38l40 40"/><path d="M78 38L38 78"/><path d="M72 34l12 12"/></g></svg>
      <div class="feature-label">FOOD</div>
    </div>
    <div class="feature" style="left:351px">
      <svg class="feature-badge" viewBox="0 0 116 116"><circle cx="58" cy="58" r="54" fill="none" stroke="var(--green)" stroke-width="3"/><circle cx="58" cy="58" r="47" fill="var(--green)"/><g stroke="#fff" stroke-width="2.6" fill="none"><path d="M36 34h20c0 14-4 20-10 20s-10-6-10-20z"/><path d="M46 54v20M38 74h16"/><path d="M62 56h16l-2 20H64z"/><circle cx="70" cy="50" r="6"/></g></svg>
      <div class="feature-label">DRINKS</div>
    </div>
    <div class="feature" style="left:520px">
      <svg class="feature-badge" viewBox="0 0 116 116"><circle cx="58" cy="58" r="54" fill="none" stroke="var(--blue)" stroke-width="3"/><circle cx="58" cy="58" r="47" fill="var(--blue)"/><g stroke="#fff" stroke-width="2.6" fill="none"><path d="M50 72V40l24-6v32"/><ellipse cx="44" cy="72" rx="6" ry="4.5"/><ellipse cx="68" cy="66" rx="6" ry="4.5"/><path d="M50 48l24-6"/></g></svg>
      <div class="feature-label">MUSIC</div>
    </div>
    <div class="feature" style="left:681px">
      <svg class="feature-badge" viewBox="0 0 116 116"><circle cx="58" cy="58" r="54" fill="none" stroke="var(--green)" stroke-width="3"/><circle cx="58" cy="58" r="47" fill="var(--green)"/><g stroke="#fff" stroke-width="2.6" fill="none"><path d="M34 38c8 4 18 4 26 0v16c0 8-6 14-13 14s-13-6-13-14z"/><path d="M58 52c8 4 18 4 26 0v16c0 8-6 14-13 14s-13-6-13-14z"/></g></svg>
      <div class="feature-label">FUN</div>
    </div>
  </section>

  <div class="abs activities">
    <p>Kids Games, Bounce Houses, Face Painting</p>
    <p>Silent &amp; Live Auction, Bake Sale, Raffes</p>
    <p>Children's Special <span class="studio">HOLLIS STUDIO</span> by 12-2 Walk-in-Appts.</p>
  </div>

  <div class="abs web">
    <svg width="34" height="34" viewBox="0 0 34 34"><circle cx="17" cy="17" r="17" fill="var(--purple)"/><g stroke="#fff" stroke-width="1.5" fill="none"><circle cx="17" cy="17" r="9"/><ellipse cx="17" cy="17" rx="4" ry="9"/><path d="M8 17h18M10 12h14M10 22h14"/></g></svg>
    <span>http/kitedayfest.org/M.A.S.O.N</span>
  </div>

  <div class="abs donate-note">
    <p>If anyone wishes to donate any items or purcahse a</p>
    <p>ticket please contact one of the following people:</p>
  </div>

  <svg class="abs phone-icon" width="38" height="38" viewBox="0 0 38 38"><circle cx="19" cy="19" r="19" fill="var(--pink)"/><g stroke="#fff" stroke-width="1.8" fill="none"><path d="M9 15c0-3 4-5 10-5s10 2 10 5l-3 2-3-2v-2h-8v2l-3 2z"/><rect x="12" y="19" width="14" height="9" rx="2"/><circle cx="19" cy="23.5" r="2"/></g></svg>

  <table class="abs contacts">
    <tr><td>Dana Brooks</td><td class="sep">:</td><td>(555) 201-4410</td></tr>
    <tr><td>Carla Benton</td><td class="sep">:</td><td>(555) 318-7725</td></tr>
    <tr><td>Mia Foster</td><td class="sep">:</td><td>(555) 402-1963</td></tr>
    <tr><td>Tess Harlow</td><td class="sep">:</td><td>(555) 402-6218</td></tr>
  </table>

  <div class="abs center-mark">
    <span class="mark-square"></span>
    <span>QT<br>Center</span>
  </div>

  <p class="abs footnote">All processed donated to Riverbend Children's Hospital Eastfield University QT Center to help find a cure! Sponsored by Family &amp; Friends of <b>M.A.S.O.N</b></p>

  <div class="abs hospital-mark">
    <span class="mark-square"></span>
    <span>Riverbend<br>Children's Hospital</span>
  </div>
</main>
</body>
</html>
```